Halvorsen Partners Business Card

Halvorsen Partners Civil Construction
Marcus Halvorsen
CEO
727-518-6094
Marcus@HalvorsenSiteworks.example
www.HalvorsenSiteworks.example
Site Development
Utility Construction
Excavation
40876 County Lane 19
Pine Hollow, FL 33519

Target Market(s)

Construction and government

Industry/Entity Type

Business

Contact Information for Business Card

I want an unique design that make a statement

Number of Pages Required

1 page

Font styles to use

Colors

Designer to choose colors to be used in the design.

Requirements
Must have
• unique design, feel free to modify or change the color of my logo.
Nice to have
• extra design features like spot UV, foil accents, color edges, unique paper, or any thing that would make my card pop.
• I like the feel of the image that I attached

```html
<!DOCTYPE html>
<html lang="en">
<head>
<meta charset="utf-8">
<title>Halvorsen Partners Business Card</title>
<link rel="stylesheet" href="https://fonts.googleapis.com/css2?family=Open+Sans:wght@400;600;700&family=Roboto+Condensed:wght@400;700&display=swap">
<style>
  :root {
    --backdrop-light: #8c8c8c;
    --backdrop-dark: #5a5a5a;
    --paper: #ffffff;
    --brand-blue: #3f5aa8;
    --band-blue: #2f4b86;
    --band-blue-light: #6c84b5;
    --silver: #b9bcc2;
    --silver-dark: #9a9da3;
    --ink-gray: #8e8e8e;
    --ink-dark: #2b2b2b;
  }
  * { margin: 0; padding: 0; box-sizing: border-box; }
  html, body { width: 1200px; height: 1199px; overflow: hidden; }
  body {
    background: radial-gradient(circle at 50% 50%, var(--backdrop-light), var(--backdrop-dark));
    font-family: "Open Sans", sans-serif;
    position: relative;
  }
  .card {
    position: absolute;
    left: 180px;
    width: 840px;
    height: 480px;
    background: var(--paper);
    box-shadow: 0 14px 30px rgba(0,0,0,0.35);
    overflow: hidden;
  }
  .card--front { top: 70px; }
  .card--back { top: 630px; }

  .wordmark { position: absolute; display: flex; align-items: center; gap: 16px; }
  .wordmark__square { width: 58px; height: 58px; background: var(--brand-blue); }
  .wordmark__divider { width: 2px; height: 62px; background: var(--silver); }
  .wordmark__name {
    font-weight: 600; color: var(--brand-blue); font-size: 34px;
    letter-spacing: 0.5px; line-height: 1; text-transform: uppercase;
  }
  .wordmark__tagline {
    font-weight: 400; color: var(--ink-gray); font-size: 17px;
    letter-spacing: 6px; text-transform: uppercase; margin-top: 6px;
  }
  .card--front .wordmark { left: 140px; top: 200px; }

  .front-url {
    position: absolute; right: 60px; bottom: 50px;
    font-size: 22px; letter-spacing: 3px; color: var(--ink-dark);
  }
  .front-url span { color: var(--brand-blue); }

  .back-art { position: absolute; inset: 0; }
  .card--back .wordmark { left: 150px; top: 40px; }
  .card--back .wordmark__square { width: 50px; height: 50px; }
  .card--back .wordmark__name { font-size: 30px; }
  .card--back .wordmark__tagline { font-size: 15px; }

  .cond { font-family: "Roboto Condensed", sans-serif; }
  .holder { position: absolute; left: 34px; top: 205px; color: var(--paper); }
  .holder__name { font-size: 30px; font-weight: 700; }
  .holder__title { font-size: 20px; margin-top: 2px; }

  .services { position: absolute; left: 318px; top: 168px; width: 500px; list-style: none; color: var(--paper); }
  .services li {
    display: flex; align-items: center; gap: 10px;
    font-size: 19px; text-transform: uppercase; line-height: 27px;
  }
  .services li::after { content: ""; flex: 1; height: 1px; background: rgba(255,255,255,0.55); }

  .address { position: absolute; right: 40px; top: 262px; text-align: right; color: var(--paper); font-size: 19px; line-height: 26px; }
  .address strong { font-weight: 700; }

  .contacts { position: absolute; left: 44px; top: 300px; list-style: none; color: var(--paper); }
  .contacts li { display: flex; align-items: center; gap: 14px; font-size: 23px; line-height: 38px; }
  .contacts svg { width: 20px; height: 20px; fill: var(--paper); flex: none; }
</style>
</head>
<body>

<section class="card card--front" aria-label="Card front">
  <div class="wordmark">
    <div class="wordmark__square"></div>
    <div class="wordmark__divider"></div>
    <div>
      <div class="wordmark__name">Halvorsen Partners</div>
      <div class="wordmark__tagline">Civil Construction</div>
    </div>
  </div>
  <p class="front-url">www.<span>HalvorsenSiteworks</span>.example</p>
</section>

<section class="card card--back" aria-label="Card back">
  <svg class="back-art" viewBox="0 0 840 480" width="840" height="480" aria-hidden="true">
    <defs>
      <linearGradient id="bandFade" x1="0" y1="1" x2="1" y2="0">
        <stop offset="0" stop-color="var(--band-blue-light)"/>
        <stop offset="0.45" stop-color="var(--band-blue)"/>
      </linearGradient>
      <linearGradient id="tabFade" x1="0" y1="0" x2="1" y2="0">
        <stop offset="0" stop-color="var(--silver-dark)"/>
        <stop offset="1" stop-color="var(--silver)"/>
      </linearGradient>
    </defs>
    <polyline points="300,154 840,154" stroke="var(--silver)" stroke-width="6" fill="none"/>
    <polygon points="0,198 292,198 266,268 0,268" fill="url(#tabFade)"/>
    <polygon points="0,268 266,268 304,160 840,160 840,420 0,420" fill="url(#bandFade)"/>
    <line x1="0" y1="432" x2="840" y2="432" stroke="var(--silver)" stroke-width="3"/>
  </svg>

  <div class="wordmark">
    <div class="wordmark__square"></div>
    <div class="wordmark__divider"></div>
    <div>
      <div class="wordmark__name">Halvorsen Partners</div>
      <div class="wordmark__tagline">Civil Construction</div>
    </div>
  </div>

  <div class="holder cond">
    <div class="holder__name">Marcus Halvorsen</div>
    <div class="holder__title">CEO</div>
  </div>

  <ul class="services cond">
    <li>Site Development</li>
    <li>Utility Construction</li>
    <li>Excavation</li>
  </ul>

  <p class="address cond">
    <strong>Halvorsen Partners Civil Construction</strong><br>
    40876 County Lane 19<br>
    Pine Hollow, FL 33519
  </p>

  <ul class="contacts cond">
    <li>
      <svg viewBox="0 0 24 24"><path d="M6.6 10.8a15 15 0 0 0 6.6 6.6l2.2-2.2a1 1 0 0 1 1-.25 11.4 11.4 0 0 0 3.6.57 1 1 0 0 1 1 1V20a1 1 0 0 1-1 1A17 17 0 0 1 3 4a1 1 0 0 1 1-1h3.5a1 1 0 0 1 1 1c0 1.250.2 2.45.57 3.57a1 1 0 0 1-.25 1z"/></svg>
      727-518-6094
    </li>
    <li>
      <svg viewBox="0 0 24 24"><path d="M2 5h20v14H2z M4 7v.5l8 5 8-5V7l-8 5z" fill-rule="evenodd"/></svg>
      Marcus@HalvorsenSiteworks.example
    </li>
    <li>
      <svg viewBox="0 0 24 24"><circle cx="12" cy="12" r="10"/></svg>
      www.HalvorsenSiteworks.example
    </li>
  </ul>
</section>

</body>
</html>
```